KV MOTORS BANNER/SIGN DESIGN

Design a banner sign for outdoor use for KV MOTORS - a premium pre owned vehicle sales center. The size must be 36 feet in width
and 3 feet in height.

Information required: logo (attached)
-PREMIUM PRE-OWEND VEHICLE SALES
- 403.555.0172

perhaps in smaller font: BUY-SELL-TRADE

prefer white background but could possibly do red matching the logo

```html
<!DOCTYPE html>
<html lang="en">
<head>
<meta charset="utf-8">
<title>KV Motors Banner</title>
<link href="https://fonts.googleapis.com/css2?family=Michroma&family=Orbitron:wght@900&family=Open+Sans:wght@400&display=swap" rel="stylesheet">
<style>
  :root {
    --red: #d0060f;
    --red-dark: #a50009;
    --ink: #1c1c1c;
    --paper: #f4f4f4;
    --paper-warm: #f7e9ea;
    --white: #ffffff;
  }
  html, body { margin: 0; padding: 0; overflow: hidden; }
  body { width: 1200px; height: 100px; background: var(--white); }
  .banner {
    position: relative;
    width: 1200px;
    height: 100px;
    overflow: hidden;
    background: linear-gradient(100deg, var(--paper-warm) 0%, var(--paper) 30%, var(--paper) 70%, #fafafa 100%);
  }
  .shapes { position: absolute; inset: 0; }
  .brand {
    position: absolute;
    left: 18px;
    top: 13px;
    display: flex;
    align-items: center;
    gap: 8px;
  }
  .brand-dot {
    width: 20px; height: 20px;
    border-radius: 50%;
    background: var(--red);
  }
  .brand-name {
    font-family: "Orbitron", sans-serif;
    font-weight: 900;
    font-size: 22px;
    letter-spacing: 1px;
    color: var(--ink);
  }
  .phone {
    position: absolute;
    left: 36px;
    top: 80px;
    display: flex;
    align-items: center;
    gap: 12px;
    font-family: "Open Sans", sans-serif;
    font-size: 10px;
    color: var(--white);
  }
  .headline {
    position: absolute;
    left: 442px;
    top: 18px;
    margin: 0;
    font-family: "Michroma", sans-serif;
    font-weight: 400;
    font-size: 16.5px;
    color: var(--ink);
    white-space: nowrap;
  }
  .headline .accent { color: var(--red); }
  .services {
    position: absolute;
    left: 443px;
    top: 60px;
    display: flex;
    margin: 0; padding: 0;
    list-style: none;
  }
  .services li {
    display: flex;
    align-items: center;
    gap: 6px;
    width: 80px;
    font-family: "Michroma", sans-serif;
    font-size: 11px;
    color: var(--ink);
  }
  .vehicle-photo {
    position: absolute;
    left: 952px;
    top: 14px;
    width: 182px;
    height: 82px;
    border-radius: 40px 60px 20px 20px;
    background: radial-gradient(ellipse at 40% 45%, #e8222a 0%, #c0060e 55%, #7a0207 100%);
  }
</style>
</head>
<body>
<div class="banner">
  <svg class="shapes" width="1200" height="100" viewBox="0 0 1200 100" aria-hidden="true">
    <polygon points="251,0 347,0 299,70" fill="var(--red)"/>
    <polygon points="10,75 155,75 145,100 0,100 0,88" fill="var(--red)"/>
    <polygon points="149,100 166,75 181,100" fill="var(--red)"/>
    <circle cx="1075" cy="118" r="128" fill="var(--red)"/>
    <circle cx="1075" cy="118" r="106" fill="var(--white)"/>
  </svg>

  <div class="brand">
    <span class="brand-dot"></span>
    <span class="brand-name">KV MOTORS</span>
  </div>

  <div class="phone">
    <svg width="9" height="9" viewBox="0 0 24 24" aria-hidden="true">
      <path fill="#fff" d="M6.6 10.8a15.1 15.1 0 0 0 6.6 6.6l2.2-2.2a1 1 0 0 1 1-.25 11.4 11.4 0 0 0 3.6.57 1 1 0 0 1 1 1V20a1 1 0 0 1-1 1A17 17 0 0 1 3 4a1 1 0 0 1 1-1h3.5a1 1 0 0 1 1 1c0 1.25.2 2.45.57 3.57a1 1 0 0 1-.25 1z"/>
    </svg>
    <span>403.555.0172</span>
  </div>

  <h1 class="headline">PREMIUM <span class="accent">PRE-OWNED</span> VEHICLE SALES</h1>

  <ul class="services">
    <li><svg width="9" height="9" viewBox="0 0 10 10" aria-hidden="true"><circle cx="5" cy="5" r="5" fill="var(--red)"/><path d="M4 2.8 6.2 5 4 7.2" stroke="#fff" stroke-width="1.5" fill="none"/></svg>BUY</li>
    <li><svg width="9" height="9" viewBox="0 0 10 10" aria-hidden="true"><circle cx="5" cy="5" r="5" fill="var(--red)"/><path d="M4 2.8 6.2 5 4 7.2" stroke="#fff" stroke-width="1.5" fill="none"/></svg>SELL</li>
    <li><svg width="9" height="9" viewBox="0 0 10 10" aria-hidden="true"><circle cx="5" cy="5" r="5" fill="var(--red)"/><path d="M4 2.8 6.2 5 4 7.2" stroke="#fff" stroke-width="1.5" fill="none"/></svg>TRADE</li>
  </ul>

  <div class="vehicle-photo" role="img" aria-label="Photo of a red premium sports sedan"></div>
</div>
</body>
</html>
```